Business Card Design

Buy and sell properties
Buy and rehab properties
Buy properties for cash
That is what I do but do need a logo
looking for some type of logo or design on it
Just started business
Back of card should say something like BUY HOUSES CASH
Overview: it is a new company. Basically I buy properties wholesale and fix them up and sell them or sell them to other fix and flippers
Background: company is new so not any background
Market: is basically anyone selling a house or buying a house. Someone that needs to sell house fast. Basically I am a cash home buyer!!!

Updates
Email on card should be:   harborlanerealtyinc@mailbox.test

Industry/Entity Type
House
Contact Information for Business Card
Harbor Lane Realty Inc
PO Box 718269
Cedar Marsh FL 32987

Dale Morrick
dmorrick@mailbox.test
555-271-6094

```html
<!DOCTYPE html>
<html lang="en">
<head>
<meta charset="utf-8">
<title>Harbor Lane Realty Inc — Business Card</title>
<link rel="stylesheet" href="https://fonts.googleapis.com/css2?family=Bitter:wght@700&family=Arimo:wght@400&display=swap">
<style>
  :root {
    --backdrop: #e9e6e1;
    --card-white: #ffffff;
    --brand-blue: #0b6db3;
    --ink: #1b1b1b;
    --hand-tone: #d9a27f;
    --note-tone: #cfd6c4;
  }
  * { margin: 0; padding: 0; box-sizing: border-box; }
  html, body { width: 1200px; height: 858px; overflow: hidden; }
  body {
    background: var(--backdrop);
    display: flex;
    align-items: center;
    justify-content: center;
    gap: 40px;
  }
  .card {
    width: 540px;
    height: 309px;
    position: relative;
    box-shadow: 0 6px 18px rgba(0,0,0,0.22);
  }
  .card-front {
    background: var(--card-white);
    display: flex;
    flex-direction: column;
    justify-content: center;
    padding-left: 70px;
  }
  .company {
    display: flex;
    align-items: center;
    gap: 12px;
    font-family: "Bitter", Georgia, serif;
    font-weight: 700;
    font-size: 25px;
    letter-spacing: 0.5px;
    color: var(--ink);
    text-transform: uppercase;
  }
  .company-mark {
    width: 18px;
    height: 18px;
    background: var(--brand-blue);
    flex: none;
  }
  .person {
    margin-top: 20px;
    margin-left: 30px;
    font-family: "Bitter", Georgia, serif;
    font-weight: 700;
    font-size: 22px;
    color: var(--brand-blue);
    text-transform: uppercase;
    letter-spacing: 0.5px;
  }
  .contact {
    margin-top: 14px;
    margin-left: 30px;
    list-style: none;
    font-family: "Arimo", Arial, sans-serif;
    font-size: 15px;
    line-height: 1.5;
    color: var(--ink);
  }
  .card-back {
    background: var(--brand-blue);
    overflow: hidden;
  }
  .cash-photo {
    position: absolute;
    left: 150px;
    top: 30px;
    width: 300px;
    height: 170px;
    border-radius: 40px 80px 60px 30px;
    background: linear-gradient(110deg, var(--hand-tone) 0%, var(--hand-tone) 40%, var(--note-tone) 60%, #b8c3ad 100%);
  }
  .tagline {
    position: absolute;
    left: 40px;
    bottom: 36px;
    font-family: "Bitter", Georgia, serif;
    font-weight: 700;
    font-size: 40px;
    color: #000;
    text-transform: uppercase;
    letter-spacing: 1px;
  }
</style>
</head>
<body>
  <section class="card card-front">
    <div class="company"><span class="company-mark"></span>Harbor Lane Realty Inc</div>
    <div class="person">Dale Morrick</div>
    <ul class="contact">
      <li>555-271-6094</li>
      <li>dmorrick@mailbox.test</li>
      <li>PO Box 718269 Cedar Marsh FL 32987</li>
    </ul>
  </section>
  <section class="card card-back">
    <div class="cash-photo" role="img" aria-label="Photo of an open hand holding a small house folded from dollar bills"></div>
    <div class="tagline">Buy Houses Cash</div>
  </section>
</body>
</html>
```